A TMV Arquitetura e Interiores desenvolve, executa e gerencia projetos de arquitetura e decoração de interiores.
Nosso objetivo é elaborar projetos com a melhor organização dos ambientes, proporcionando ao cliente a otimização dos espaços aumentando assim, a qualidade de vida, o conforto e o bem estar de seus moradores.
Gostaríamos que o site fosse clean, leve, moderno, chique e que valorizasse as fotos dos nossos trabalhos. Seria legal usarmos as cores da nossa logo para compor o site.
Na home, gostaríamos que entrassem os seguintes itens:
Quem somos / Projetos / Imprensa / Novidades / Contato
Abaixo seguem alguns sites de referência:
www.carladorneles.com.br
www.soniaquevedo.com.br
www.lucianafontoura.com.br
www.tedmarchbank.co.uk
www.dksarquitetura.com.br
Em anexo segue a nossa logo e cartões de visita para consulta.

```html
<!DOCTYPE html>
<html lang="pt-BR">
<head>
<meta charset="utf-8">
<title>TMV Arquitetura e Interiores</title>
<link rel="stylesheet" href="https://fonts.googleapis.com/css2?family=Mulish:wght@400;500;600&display=swap">
<style>
  :root {
    --brand-green: #4a9a44;
    --brand-green-light: #6fb35f;
    --panel-dark: rgba(18, 18, 18, 0.86);
    --text-light: #ffffff;
    --text-dark: #1e1e1e;
    --text-muted: #4a4a4a;
    --dot-idle: #cfcfcf;
    --page-bg: #ffffff;
  }
  * { margin: 0; padding: 0; box-sizing: border-box; }
  html, body {
    width: 1200px; height: 923px; overflow: hidden;
    background: var(--page-bg);
    font-family: "Mulish", "Helvetica Neue", Arial, sans-serif;
  }
  .page { position: relative; width: 1200px; height: 923px; }

  .hero { position: absolute; left: 0; top: 0; width: 1200px; height: 796px; overflow: hidden; }
  .hero-photo {
    position: absolute; inset: 0;
    background:
      linear-gradient(180deg, rgba(255,255,255,0) 0%, rgba(255,255,255,0) 55%, rgba(120,95,70,0.35) 75%, rgba(90,80,70,0.55) 100%),
      radial-gradient(ellipse at 48% 38%, #cfe2f1 0%, #b9cfe0 22%, rgba(220,215,205,0) 48%),
      linear-gradient(90deg, #ebe6dd 0%, #f3efe8 30%, #d9dde0 55%, #e8e3da 100%);
  }
  .hero-panel {
    position: absolute; left: 776px; top: 0; width: 314px; height: 796px;
    background: var(--panel-dark);
  }
  .hero-caption { position: absolute; left: 799px; top: 584px; color: var(--text-light); }
  .hero-kicker { font-size: 24px; font-weight: 500; line-height: 28px; letter-spacing: 0.2px; }
  .hero-kicker .accent { color: var(--brand-green-light); }
  .hero-title { font-size: 44px; font-weight: 600; line-height: 44px; margin-top: 2px; letter-spacing: 0.5px; }
  .hero-text { font-size: 17px; line-height: 24px; margin-top: 6px; width: 270px; font-weight: 400; }

  .slider-dots { position: absolute; left: 799px; top: 768px; display: flex; gap: 8px; }
  .slider-dot { width: 19px; height: 6px; background: var(--dot-idle); }
  .slider-dot.is-active { background: var(--brand-green); }

  .social-tabs { position: absolute; right: 0; top: 112px; width: 38px; }
  .social-tabs svg { display: block; margin-bottom: 4px; }

  .site-header { position: absolute; left: 0; top: 796px; width: 1200px; height: 127px; }
  .brand { position: absolute; left: 110px; top: 10px; width: 240px; }
  .brand-mark {
    position: absolute; left: 73px; top: 0; width: 75px; height: 65px;
    background: linear-gradient(160deg, var(--brand-green-light), var(--brand-green));
    border-radius: 4px;
  }
  .brand-name {
    position: absolute; left: 0; top: 79px; white-space: nowrap;
    font-size: 10.5px; letter-spacing: 3.4px; color: var(--text-muted); font-weight: 500;
  }
  .main-nav { position: absolute; top: 56px; left: 589px; display: flex; gap: 29px; }
  .main-nav a {
    font-size: 14px; font-weight: 500; color: var(--text-dark);
    text-decoration: none; letter-spacing: 0.2px;
  }
  .main-nav a.is-current { color: var(--brand-green); }
</style>
</head>
<body>
<div class="page">
  <section class="hero">
    <div class="hero-photo" role="img" aria-label="Fotografia de sala de estar clara com janelas amplas, cortinas brancas, sofá, mesa de vidro e vista para montanhas"></div>
    <div class="hero-panel"></div>
    <div class="hero-caption">
      <p class="hero-kicker"><span class="accent">TMV</span> ARCHITECTURE</p>
      <h1 class="hero-title">&amp;INTERIOR</h1>
      <p class="hero-text">Develops, executes &amp; manages projects of architecture and interior decoration</p>
    </div>
    <div class="slider-dots">
      <span class="slider-dot is-active"></span>
      <span class="slider-dot"></span>
      <span class="slider-dot"></span>
      <span class="slider-dot"></span>
    </div>
    <div class="social-tabs" aria-label="Redes sociais">
      <svg width="38" height="32" viewBox="0 0 38 32"><polygon points="8,0 38,0 38,32 8,32 0,16" fill="var(--brand-green)"/></svg>
      <svg width="38" height="32" viewBox="0 0 38 32"><polygon points="8,0 38,0 38,32 8,32 0,16" fill="var(--brand-green)"/></svg>
    </div>
  </section>

  <header class="site-header">
    <div class="brand">
      <div class="brand-mark"></div>
      <p class="brand-name">TMV ARQUITETURA E INTERIORES</p>
    </div>
    <nav class="main-nav">
      <a href="#" class="is-current">QUEM SOMOS</a>
      <a href="#">PROJETOS</a>
      <a href="#">IMPRENSA</a>
      <a href="#">NOVIDADES</a>
      <a href="#">CONTATO</a>
    </nav>
  </header>
</div>
</body>
</html>
```